Box design for superfood powders

Hey,
I am creating a new brand of superfoods mixes in and I am looking for a designer to create the design for the box.
I have for 4 products on the roadmap, but I need the design just for the first one:
- For skin nails and hair benefits: Collagen + CoQ10 and Vitamin C powders (eg: Blueberries, Camu Camu, Acai)
- For energy and immune system (eg: mushrooms powder)
- Green Mix (eg: Spirulina + Wheatgrass + Chlorella)
- Protein mix (eg: hemp + rice powders)
I will use Kraft paper for the box so I am able to print max 2 colors on them (black and another color distinctive for each specific powder mix).
I need the design just for the first one with collagen, because all the products will have the same format. I will just change the name, ingredients and the color
More details in the archive attached.

Updates
Low design quality
Target Market(s)
woman between 30-50
Requirements
Should not have
- Ilustrations with fruits or flowers
Just shapes and colors

```html
<!DOCTYPE html>
<html lang="en">
<head>
<meta charset="utf-8">
<title>Radiant Collagen – box and sachet artwork</title>
<link rel="stylesheet" href="https://fonts.googleapis.com/css2?family=Poppins:ital,wght@0,400;0,500;0,600;0,700;0,800;1,800&display=swap">
<style>
:root{
  --brand-red:#a81e24;
  --ink:#111111;
  --paper:#ffffff;
  --text:#1c1c1c;
}
*{box-sizing:border-box;margin:0;padding:0}
html,body{width:708px;height:1200px;overflow:hidden;background:var(--paper)}
body{position:relative;font-family:'Poppins',sans-serif;color:var(--text)}
.panel{position:absolute}
.band{position:absolute;left:0;right:0;background:var(--brand-red);color:var(--paper)}
.product-title{display:flex;align-items:center;justify-content:center;font-weight:800;font-style:italic;letter-spacing:.2px}
.brand{position:absolute;left:0;right:0;display:flex;align-items:center;justify-content:center;gap:6px;font-weight:800;color:var(--ink);line-height:1}
.brand-dot{background:var(--brand-red);display:inline-block}
.tagline{position:absolute;left:0;right:0;text-align:center;color:var(--brand-red);font-weight:400;letter-spacing:2px}
.tear-line{position:absolute;left:0;right:0;border-top:1px dashed #555}
.tear-note{position:absolute;left:0;right:0;text-align:center;color:var(--brand-red);font-weight:600}
.story{position:absolute;left:0;right:0;background:var(--brand-red);color:var(--paper)}
.story p{text-align:justify}
.count{position:absolute;font-weight:700;color:var(--paper);display:flex;align-items:center;gap:4px}
.count .boxed{border-left:2px double var(--paper);border-right:2px double var(--paper);padding:0 2px;line-height:1}
.badges{display:flex;align-items:center;justify-content:space-evenly;padding:0 8px}
.badge{border:1.2px solid var(--paper);border-radius:50%}
.free-from{position:absolute;left:0;right:0;text-align:center;font-weight:600;color:var(--ink)}
.label-copy{position:absolute;color:var(--ink)}
.label-copy .key{color:var(--brand-red);font-weight:600}
.label-copy .maker{color:var(--brand-red);font-weight:600}
.connect{position:absolute;color:var(--paper);line-height:1.15}
.connect strong{font-weight:600}
.nutrition{position:absolute;border:1.2px solid var(--paper);color:var(--paper);display:flex;padding:2px}
.nutrition .head{border-right:1px solid var(--paper);padding-right:3px;display:flex;flex-direction:column}
.nutrition .head .t{font-weight:700;line-height:.95}
.nutrition .head .cal{margin-top:auto;font-weight:700;display:flex;align-items:flex-end;gap:2px;line-height:1}
.nutrition .head .cal span{line-height:.9}
.nutrition .body{flex:1;padding-left:3px;display:flex;flex-direction:column}
.nutrition .cols{display:flex;gap:6px}
.nutrition .col{flex:1}
.nutrition .row{display:flex;justify-content:space-between;border-bottom:.6px solid var(--paper)}
.nutrition .row.hd{font-weight:600}
.nutrition .in{padding-left:5px}
.nutrition .foot{margin-top:auto;letter-spacing:.3px}
</style>
</head>
<body>

<section class="panel box-front" style="left:94px;top:266px;width:249px;height:380px">
  <div class="band product-title" style="top:0;height:34px;font-size:21px">Radiant Collagen</div>
  <div class="brand" style="top:92px;font-size:33px"><span class="brand-dot" style="width:10px;height:10px"></span>vellora</div>
  <div class="tagline" style="top:138px;font-size:11px">Elevate your everyday glow</div>
  <div class="tear-line" style="top:229px"></div>
  <div class="tear-note" style="top:238px;font-size:9.6px">RIP-IT OFF AND START YOUR SUPERCHARGE ON</div>
  <div class="tear-line" style="top:260px"></div>
  <div class="story" style="top:260px;height:120px;padding:5px 16px 0 17px;font-size:7.6px;line-height:1.33">
    <p>We make it easy for busy people to look and feel good about their appearance. Just add Radiant Collagen powder to your favorite smoothie or milk and get the extra dose of collagen and skin protecting antioxidants. It helps combat the effects of free radicals and may restore your natural plumpness.</p>
  </div>
  <div class="count" style="right:21px;top:344px;font-size:17px"><span class="boxed">14</span>x 10g</div>
</section>

<section class="panel box-back" style="left:365px;top:266px;width:249px;height:380px">
  <div class="band badges" style="top:0;height:34px" role="img" aria-label="Free-from badges: gluten, dairy, soy, GMO, sweeteners, fillers, additives">
    <span class="badge" style="width:25px;height:25px"></span><span class="badge" style="width:25px;height:25px"></span><span class="badge" style="width:25px;height:25px"></span><span class="badge" style="width:25px;height:25px"></span><span class="badge" style="width:25px;height:25px"></span><span class="badge" style="width:25px;height:25px"></span><span class="badge" style="width:25px;height:25px"></span>
  </div>
  <div class="free-from" style="top:44px;font-size:6.8px;line-height:1.45">Free from: Gluten, Dairy, Soy, GMO, sweeteners, fillers,<br>additives, preservatives or anything artificial.</div>
  <div class="label-copy" style="left:14px;right:10px;top:160px;font-size:7.8px;line-height:1.35">
    <p class="key">Ingredients :</p>
    <p>CoQ10,Hyaluronic acid powder, Camu Camu, Rosehip, Sea buckthorn, Banana, Date, Acai</p>
    <p style="margin-top:7px"><span class="key">How to use it :</span> Add one pack to your water, smoothies, yoghurt, musli, oatmeal</p>
    <p style="margin-top:7px"><span class="key">Storage :</span> Keep closed in a cool dry place</p>
    <p style="margin-top:4px">Produced by : <span class="maker">Norla SRL for Brightpeak SRL</span></p>
  </div>
  <div class="band" style="top:260px;height:120px"></div>
  <div class="connect" style="left:14px;top:268px;font-size:7.2px"><strong>Connect :</strong><br>Call +40 000 0000 000 or<br>visit our website www.vellora.com/ro/start</div>
  <div class="nutrition" style="left:13px;top:297px;width:223px;height:61px;font-size:4.6px">
    <div class="head" style="width:55px">
      <span class="t" style="font-size:10px">Nutrition<br>Facts</span>
      <span style="font-size:6px;margin-top:3px;line-height:1.1">Serving Size<br>1 Sachet (10g)</span>
      <span class="cal" style="font-size:5.5px">Calories<span style="font-size:11px">100</span></span>
    </div>
    <div class="body">
      <div class="cols">
        <div class="col">
          <div class="row hd"><span>Amount/Serving</span><span>% DV</span></div>
          <div class="row"><span>Total Fat - 5g</span><span>6%</span></div>
          <div class="row in"><span>Saturated Fat - 1g</span><span>5%</span></div>
          <div class="row in"><span>Trans Fat - 0g</span><span></span></div>
          <div class="row"><span>Cholesterol - 0mg</span><span>0%</span></div>
          <div class="row"><span>Sodium - 0mg</span><span>0%</span></div>
        </div>
        <div class="col">
          <div class="row hd"><span>Amount/Serving</span><span>% DV</span></div>
          <div class="row"><span>Total Carbohydrate - 12g</span><span>4%</span></div>
          <div class="row in"><span>Dietary Fiber - 3g</span><span>11%</span></div>
          <div class="row in"><span>Total Sugars - 11g</span><span></span></div>
          <div class="row in"><span>Includes 0g Added Sugars</span><span></span></div>
          <div class="row"><span>Protein - 2g</span><span>0%</span></div>
        </div>
      </div>
      <div class="foot">Vitamin D 0% - Calcium 0% - Iron 0% - Potassium 0%</div>
    </div>
  </div>
</section>

<section class="panel sachet-front" style="left:159px;top:673px;width:183px;height:227px">
  <div class="band product-title" style="top:0;height:25px;font-size:15px">Radiant Collagen</div>
  <div class="brand" style="top:49px;font-size:20px"><span class="brand-dot" style="width:7px;height:7px"></span>vellora</div>
  <div class="tagline" style="top:79px;font-size:7.4px;letter-spacing:1.4px">Elevate your everyday glow</div>
  <div class="story" style="top:139px;height:88px;padding:6px 19px 0 19px;font-size:5.7px;line-height:1.33">
    <p>We make it easy for busy people to look and feel good about their appearance. Just add Radiant Collagen powder to your favorite smoothie or milk and get the extra dose of collagen and skin protecting antioxidants. It helps combat the effects of free radicals and may restore your natural plumpness.</p>
  </div>
  <div class="count" style="right:18px;top:198px;font-size:11px">10g</div>
</section>

<section class="panel sachet-back" style="left:366px;top:673px;width:183px;height:227px">
  <div class="band badges" style="top:0;height:25px;padding:0 12px" role="img" aria-label="Free-from badges: gluten, dairy, soy, GMO, sweeteners, fillers, additives">
    <span class="badge" style="width:17px;height:17px"></span><span class="badge" style="width:17px;height:17px"></span><span class="badge" style="width:17px;height:17px"></span><span class="badge" style="width:17px;height:17px"></span><span class="badge" style="width:17px;height:17px"></span><span class="badge" style="width:17px;height:17px"></span><span class="badge" style="width:17px;height:17px"></span>
  </div>
  <div class="free-from" style="top:30px;font-size:4.4px;line-height:1.55">Free from: Gluten, Dairy, Soy, GMO, sweeteners, fillers,<br>additives, preservatives or anything artificial.</div>
  <div class="label-copy" style="left:16px;right:10px;top:80px;font-size:5px;line-height:1.35">
    <p class="key">Ingredients :</p>
    <p>CoQ10,Hyaluronic acid powder, Camu Camu, Rosehip, Sea buckthorn, Banana, Date, Acai</p>
    <p style="margin-top:2px"><span class="key">How to use it :</span> Add one pack to your water, smoothies, yoghurt, musli, oatmeal</p>
    <p><span class="key">Storage :</span> Keep closed in a cool dry place</p>
    <p style="margin-top:2px">Produced by : <span class="maker">Norla SRL for Brightpeak SRL</span></p>
  </div>
  <div class="band" style="top:139px;height:88px"></div>
  <div class="connect" style="left:17px;top:144px;font-size:5px"><strong>Connect :</strong><br>Call +40 000 0000 000 or<br>visit our website www.vellora.com/ro/start</div>
  <div class="nutrition" style="left:16px;top:167px;width:152px;height:42px;font-size:3.2px;padding:1.5px">
    <div class="head" style="width:38px">
      <span class="t" style="font-size:7px">Nutrition<br>Facts</span>
      <span style="font-size:4.2px;margin-top:2px;line-height:1.1">Serving Size<br>1 Sachet (10g)</span>
      <span class="cal" style="font-size:3.8px">Calories<span style="font-size:8px">100</span></span>
    </div>
    <div class="body">
      <div class="cols">
        <div class="col">
          <div class="row hd"><span>Amount/Serving</span><span>% DV</span></div>
          <div class="row"><span>Total Fat - 5g</span><span>6%</span></div>
          <div class="row in"><span>Saturated Fat - 1g</span><span>5%</span></div>
          <div class="row in"><span>Trans Fat - 0g</span><span></span></div>
          <div class="row"><span>Cholesterol - 0mg</span><span>0%</span></div>
          <div class="row"><span>Sodium - 0mg</span><span>0%</span></div>
        </div>
        <div class="col">
          <div class="row hd"><span>Amount/Serving</span><span>% DV</span></div>
          <div class="row"><span>Total Carbohydrate - 12g</span><span>4%</span></div>
          <div class="row in"><span>Dietary Fiber - 3g</span><span>11%</span></div>
          <div class="row in"><span>Total Sugars - 11g</span><span></span></div>
          <div class="row in"><span>Includes 0g Added Sugars</span><span></span></div>
          <div class="row"><span>Protein - 2g</span><span>0%</span></div>
        </div>
      </div>
      <div class="foot">Vitamin D 0% - Calcium 0% - Iron 0% - Potassium 0%</div>
    </div>
  </div>
</section>

</body>
</html>
```